Web page for analytics company

Now that I have a new logo, I need a webpage design that will use it to its potential. Am looking for a design that handles presentation and access to data well - like sites with blocks that provide direct access to content without going through a set of menus. More like an infographic. No left/right menu bar.

I want the logo (attached) against a black background, but not text - not a fan of trying to read white text on a dark screen.

The website - morvilent.com - currently has four pages - home, who we are, by the numbers and a blog.

The site will be done in Squarespace.

My apologies for not responding promptly - big report due today.  I will be online tomorrow with answers and feedback. 

Thanks!

```html
<!DOCTYPE html>
<html lang="en">
<head>
<meta charset="utf-8">
<title>Morvilent – Gender Equity Analytics</title>
<link href="https://fonts.googleapis.com/css2?family=Questrial&display=swap" rel="stylesheet">
<style>
:root{
  --black:#000;
  --ink:#1a1a1a;
  --text:#444;
  --muted:#666;
  --orange:#f7941d;
  --grey-band:#ececec;
  --line:#dcdcdc;
  --white:#fff;
}
*{margin:0;padding:0;box-sizing:border-box}
html,body{width:802px;height:1200px;overflow:hidden;background:var(--white)}
body{font-family:"Questrial",sans-serif;color:var(--ink);position:relative}
.abs{position:absolute}
.site-header{left:0;top:0;width:802px;height:53px;background:var(--black)}
.brand{left:134px;top:12px;display:flex;align-items:center;gap:6px;color:var(--white);font-size:21px}
.brand-dot{width:26px;height:26px;border-radius:50%;background:var(--orange)}
.menu-icon{left:647px;top:18px}
.hero{left:0;top:53px;width:802px;height:293px;
  background:linear-gradient(100deg,#8e9aa0 0%,#c4ccd1 25%,#5a7fb0 40%,#d9dfe2 60%,#c2ccd1 100%)}
.hero-title{left:210px;top:193px;width:382px;height:40px;background:rgba(255,255,255,.85);text-align:center}
.hero-title h1{font-weight:400;font-size:18px;line-height:20px;padding-top:5px;letter-spacing:-.2px}
.hero-title p{font-size:12px;line-height:13px;color:#333}
.hero-quote{left:228px;top:239px;width:349px;height:25px;background:rgba(255,255,255,.85);text-align:center;font-size:8.4px;line-height:10px;color:#444;padding-top:2px}
h2{font-weight:400;font-size:26px;text-align:center;letter-spacing:-.5px;color:var(--black)}
.testimonial h2{position:absolute;left:0;width:802px;top:386px}
.quote-box{left:165px;top:425px;width:472px;height:51px;border:1px solid var(--line);text-align:center;font-size:9.4px;line-height:15.5px;color:var(--muted);padding-top:9px}
.quote-tail{left:393px;top:475px;width:10px;height:10px;background:var(--white);border-right:1px solid var(--line);border-bottom:1px solid var(--line);transform:rotate(45deg) scale(.7)}
.quote-source{left:0;width:802px;top:488px;text-align:center;font-size:8px;color:#222}
.btn{background:var(--orange);color:var(--white);text-align:center;font-size:9.6px}
.btn-more{left:363px;top:509px;width:75px;height:20px;line-height:20px}
.about{left:0;top:562px;width:802px;height:240px;background:var(--grey-band)}
.about h2{position:absolute;top:23px;width:802px}
.about-text{left:134px;top:59px;width:534px;text-align:center;font-size:8.1px;line-height:13.6px;color:#333}
.about-text strong{font-weight:400;color:var(--black);text-shadow:0 0 .3px #000}
.subscribe h2{position:absolute;left:0;width:802px;top:839px}
.field{left:199px;width:404px;height:23px;border:1px solid var(--line);font-size:7.2px;color:#777;padding:8px 0 0 15px}
.btn-sub{left:350px;top:992px;width:101px;height:19px;line-height:19px}
.rule{left:0;width:802px;height:1px;background:#e6e6e6}
.tweet{top:1069px;width:160px}
.tweet h3{font-weight:400;font-size:10px;color:var(--black);margin-bottom:3px}
.tweet p{font-size:6.8px;line-height:11.8px;color:#444}
.tweet time{display:block;font-size:6.8px;line-height:11.8px;color:var(--black);text-shadow:0 0 .3px #000}
.follow{left:134px;top:1141px;height:10px;padding:0 4px;border:1px solid #bbb;background:linear-gradient(#fafafa,#dcdcdc);font-size:6px;line-height:9px;color:#1f5f9a}
.copyright{left:135px;top:1179px;font-size:8px;color:#333}
</style>
</head>
<body>
<header class="site-header abs">
  <div class="brand abs"><span class="brand-dot"></span><span>Morvilent</span></div>
  <svg class="menu-icon abs" width="21" height="18" viewBox="0 0 21 18" aria-label="Menu">
    <rect y="0" width="21" height="2.6" fill="#fff"/><rect y="5" width="21" height="2.6" fill="#fff"/>
    <rect y="10" width="21" height="2.6" fill="#fff"/><rect y="15" width="21" height="2.6" fill="#fff"/>
  </svg>
</header>

<section class="hero abs" role="img" aria-label="Photo of a smiling man working on a laptop in a bright office"></section>
<div class="hero-title abs"><h1>GENDER EQUITY ANALYTICS</h1><p>Enhancing Performance Through A Gender Lens</p></div>
<div class="hero-quote abs">“we Keep Statistics On Everything We Care About, From Rbis To Roi, The Daily<br>Ups And Downs Of The Dow And Our Bank Accounts...</div>

<section class="testimonial">
  <h2>What People Says</h2>
  <div class="quote-box abs">So If We’re Serious About Narrowing The Gender Gap And Helping More Girls And Women,<br>Then We Must Get Serious About Gathering And Analyzing The Data That Tell The Tale.”</div>
  <div class="quote-tail abs"></div>
  <p class="quote-source abs">- Former Secretary of State Eleanor Vance Whitmore, July 2012-</p>
  <div class="btn btn-more abs">View More</div>
</section>

<section class="about abs">
  <h2>About us</h2>
  <div class="about-text abs">
    As much as we’d like to think that treating everyone equally is the best strategy for fairness, the reality is that the differences in the lives of women and men have to be taken into account to ensure that organizations, programs, services, and yes, even public policy treat women and men in ways that achieve gender equity.<br>
    That’s where Morvilent - Gender Equity Analytics - comes in. Using the data-driven tools of gender analysis, we can help you determine if gender equity is being achieved - in businesses and organizations, in the planning and implementation of programs and services, and in the development and enforcement of public policy.<br>
    The evidence is in: analysis of organizational performance metrics that date back to the 1980s shows there is a clear relationship between better results and diverse leadership. Senior executives who ignore the data do so to their detriment. They’re literally leaving money on the table.<br>
    But numbers don’t tell the whole story. Organizations have to be willing to dig deep to discover where the biases are buried - in the organization’s culture, in governance practices, in talent management strategies, and in personal values and belief systems.<br>
    Find out what a gender equity audit can do for your organization. Contact us at <strong>hlarsen@morvilent.com or 555-014-2287.</strong>
  </div>
</section>

<section class="subscribe">
  <h2>Subscribe To Our Mailing List</h2>
  <div class="field abs" style="top:889px">Email Address</div>
  <div class="field abs" style="top:922px">First Name</div>
  <div class="field abs" style="top:954px">Last Name</div>
  <div class="btn btn-sub abs">Suscribe Now</div>
</section>

<div class="rule abs" style="top:1051px"></div>

<section class="tweets">
  <article class="tweet abs" style="left:137px">
    <h3>Center for Parity Studies</h3>
    <p>Swedish video closes the gender pay gap in 47 seconds: we just need to "be a man!" Chatterly app let's you try it. http://lnk.to/Qr7Pd2</p>
    <time>about a day ago</time>
  </article>
  <article class="tweet abs" style="left:317px">
    <h3>Center for Parity Studies</h3>
    <p>Marlowe describes life-stage approach Kestrel Ltd. takes to women's career advancement. #equalitymeansjobs More info: http://lnk.to/Hw4Km9</p>
    <time>about 5 days ago</time>
  </article>
  <article class="tweet abs" style="left:497px">
    <h3>Center for Parity Studies</h3>
    <p>Need to stop using "choices" as an excuse for gender inequality. Brightwell says even w/ same choices women do less well. #equalitymeansjobs</p>
    <time>about 5 days ago</time>
  </article>
  <div class="follow abs">Follow @Parity_Center</div>
</section>

<div class="rule abs" style="top:1169px"></div>
<footer class="copyright abs">Copyright © 2014 Morvilent. All rights reserved.</footer>
</body>
</html>
```